Business Card Design using new attached logo

We are a family run Plumbing and Heating firm looking to improve our company image with an improved business card and new logo.We are looking to keep the company colour (Blue) involved in our design

Reason: New logo added which needs to be incorporated on designs

Industry/Entity Type

Business

Contact Information for Business Card

See attachment of all info required.

Requirements
Must have
• We have just picked a new company logo which is attached.
• Could you please provide your business card designs using this logo.
• We are looking for the logo on the back as well as the front with all the info required

```html
<!DOCTYPE html>
<html lang="en">
<head>
<meta charset="utf-8">
<title>BLX Services – Business Cards</title>
<link rel="stylesheet" href="https://fonts.googleapis.com/css2?family=Questrial&display=swap">
<style>
  :root {
    --navy: #1c3466;
    --paper: #f3f3f3;
    --backdrop: #e4e5e7;
    --ink-grey: #5b6170;
    --white: #ffffff;
  }
  * { box-sizing: border-box; margin: 0; padding: 0; }
  html, body {
    width: 1200px; height: 1200px; overflow: hidden;
    background: var(--backdrop);
    font-family: "Questrial", "Century Gothic", sans-serif;
  }
  .sheet {
    width: 1200px; height: 1200px;
    display: flex; flex-direction: column; align-items: center; justify-content: center;
    gap: 50px;
  }
  .card {
    position: relative;
    width: 840px; height: 509px;
    background: var(--paper);
    overflow: hidden;
    box-shadow: 0 10px 30px rgba(0,0,0,0.12);
  }

  /* Front */
  .front .band {
    position: absolute; left: 0; right: 0; height: 34px; background: var(--navy);
  }
  .front .band--top { top: 14px; }
  .front .band--bottom { bottom: 14px; }
  .front .brand {
    position: absolute; left: 0; right: 0; top: 170px;
    display: flex; align-items: center; justify-content: center; gap: 18px;
  }
  .brand-dot {
    width: 30px; height: 30px; border-radius: 50%; background: var(--navy);
  }
  .brand-name {
    color: var(--navy); font-size: 74px; letter-spacing: 2px; line-height: 1;
  }
  .front .website {
    position: absolute; left: 0; right: 0; top: 290px;
    text-align: center; color: var(--navy); font-size: 42px;
  }

  /* Back */
  .back .stripe {
    position: absolute; left: 0; top: 160px; width: 470px; height: 16px; background: var(--navy);
  }
  .back .panel-right {
    position: absolute; left: 470px; top: 160px; right: 0; bottom: 0; background: var(--navy);
  }
  .back .panel-left {
    position: absolute; left: 0; top: 292px; width: 470px; bottom: 0; background: var(--navy);
  }
  .back .person {
    position: absolute; right: 34px; top: 84px; text-align: right;
  }
  .person-name { color: var(--navy); font-size: 34px; font-weight: 700; line-height: 1; }
  .person-role { color: var(--ink-grey); font-size: 20px; margin-top: 2px; }
  .back .brand {
    position: absolute; left: 34px; top: 205px;
    display: flex; align-items: center; gap: 12px;
  }
  .back .brand-dot { width: 20px; height: 20px; }
  .back .brand-name { font-size: 48px; }
  .contacts {
    position: absolute; left: 34px; top: 322px;
    list-style: none; color: var(--white); font-size: 25px;
  }
  .contacts li { display: flex; align-items: center; gap: 10px; height: 38px; }
  .contacts svg { width: 20px; height: 20px; flex: none; }
  .address {
    position: absolute; left: 520px; top: 200px;
    color: var(--white); font-size: 27px; line-height: 1.3; font-style: normal;
  }
</style>
</head>
<body>
<main class="sheet">

  <section class="card front" aria-label="Business card front">
    <div class="band band--top"></div>
    <div class="band band--bottom"></div>
    <div class="brand">
      <span class="brand-dot"></span>
      <span class="brand-name">BLX SERVICES</span>
    </div>
    <p class="website">blxservicesltd.co.uk</p>
  </section>

  <section class="card back" aria-label="Business card back">
    <div class="stripe"></div>
    <div class="panel-right"></div>
    <div class="panel-left"></div>

    <div class="person">
      <p class="person-name">Daniel Hart</p>
      <p class="person-role">Director</p>
    </div>

    <div class="brand">
      <span class="brand-dot"></span>
      <span class="brand-name">BLX SERVICES</span>
    </div>

    <ul class="contacts">
      <li>
        <svg viewBox="0 0 20 20" aria-hidden="true"><rect x="5" y="1" width="10" height="18" rx="2" fill="#fff"/><rect x="7" y="4" width="6" height="10" fill="#1c3466"/></svg>
        07700900123
      </li>
      <li>
        <svg viewBox="0 0 20 20" aria-hidden="true"><rect x="1.5" y="4" width="17" height="12" fill="none" stroke="#fff" stroke-width="2"/><path d="M2 5 L10 11 L18 5" fill="none" stroke="#fff" stroke-width="2"/></svg>
        danielhart@blxservicesltd.co.uk
      </li>
      <li>
        <svg viewBox="0 0 20 20" aria-hidden="true"><path d="M5 2 L8 6 L6.5 8 Q8.5 12 12 13.5 L14 12 L18 15 L16 18 Q8 18 2 5 Z" fill="#fff"/></svg>
        020 7946 0321
      </li>
      <li>
        <svg viewBox="0 0 20 20" aria-hidden="true"><rect x="5" y="2" width="10" height="5" fill="#fff"/><rect x="2" y="8" width="16" height="7" rx="1" fill="#fff"/><rect x="5" y="13" width="10" height="5" fill="#fff" stroke="#1c3466" stroke-width="1"/></svg>
        020 7946 0874
      </li>
    </ul>

    <address class="address">
      14 Mill Parade<br>
      Kestrel Road<br>
      Fairbridge<br>
      FB27QL
    </address>
  </section>

</main>
</body>
</html>
```